Rug Cleaning Web Design Project

We need a web design for our cleaning company. We currently have a web page but are not happy with its design. We currently offer fine rug cleaning,upholstery cleaning, and residential and commercial carpet cleanning. We also offer water damage restoration. For our rug cleaning services we offer : Enzyme treatments for pet contamination and odor removal, application of stain protection that is designed for the fine textiles used in rug construction, application of treatments designed to prevent moth damage and pads designed to be used under rugs.Our current web site is harborfreshcare.example. We are intrested in a design with similar information to the web page of Velmora Rug Cleaners INC. We would like to use the colors that are present in our logo that will be uploaded with this description. We would also like this new page to be linked to our other address loomrinsepro.example. We would like the deign to be visually attractive but not "too busy".
Updates

Please include pictures of rugs, or people washing rugs if possible. We do not offer maid type cleaning services. We would not be interested in designs including pictures depicting that type service. Thanks for your hard work on this project.

Dana Whitlow

Industry/Entity Type

Residential

Requirements
Must have
• This page must be viewable on smart phones and tablets.

```html
<!DOCTYPE html>
<html lang="en">
<head>
<meta charset="utf-8">
<title>LoomRinsePro – Harborfresh Cleaning, LLC</title>
<link rel="stylesheet" href="https://fonts.googleapis.com/css2?family=Open+Sans:wght@400;600;700&family=Montserrat:wght@300;400;600&family=Lora:ital@1&display=swap">
<style>
:root{
  --blue:#1f86cf;
  --blue-dark:#0a5ea8;
  --blue-light:#4aa6e4;
  --text:#555b60;
  --heading-grey:#7a7f84;
  --badge:#4b4c4e;
  --white:#ffffff;
}
*{box-sizing:border-box;margin:0;padding:0}
html,body{width:985px;height:1200px;overflow:hidden;background:var(--white)}
body{position:relative;font-family:"Open Sans",Arial,sans-serif;color:var(--text)}

.site-header{position:absolute;left:0;top:0;width:985px;height:140px;
  background:linear-gradient(180deg,var(--blue-light) 0%,var(--blue) 55%,var(--blue-dark) 100%)}
.header-tab{position:absolute;left:0;top:0}
.brand{position:absolute;left:350px;top:12px;display:flex;align-items:center;gap:12px}
.brand-mark{width:44px;height:44px;border-radius:50%;background:var(--blue)}
.brand-name{font-weight:700;font-size:30px;color:#2a2a2a;letter-spacing:-.5px;line-height:1}

.main-nav{position:absolute;left:116px;top:105px;width:752px;height:35px;display:flex;
  background:linear-gradient(180deg,#3e9ee0,#1e7fc8);border:1px solid #5fb2ea;border-bottom:none;border-radius:6px 6px 0 0}
.main-nav a{color:var(--white);text-decoration:none;font-weight:600;font-size:16px;display:flex;align-items:center;justify-content:center;border-right:1px solid #1868ab}
.main-nav a:last-child{border-right:none}

.hero-band{position:absolute;left:0;top:140px;width:985px;height:372px;
  background:radial-gradient(ellipse at 50% 40%,#e4e5e6 0%,#c3c5c7 70%,#b3b5b7 100%)}
.hero-frame{position:absolute;left:116px;top:172px;width:752px;height:309px;background:var(--white);border-radius:5px;padding:4px;box-shadow:0 2px 6px rgba(0,0,0,.25)}
.hero-photo{width:100%;height:100%;border-radius:3px;
  background:linear-gradient(100deg,#8a4a22 0%,#c06a2a 25%,#b78a4a 45%,#d9962a 65%,#c9a245 80%,#7a4a25 100%)}
.slider-dots{position:absolute;left:405px;top:467px;display:flex;gap:2px}
.slider-dots span{width:42px;height:3px;background:rgba(0,0,0,.35)}
.slider-dots span.active{background:#111}

.welcome{position:absolute;left:116px;top:540px;width:560px}
.welcome-kicker{font-family:"Montserrat",Arial,sans-serif;font-weight:300;font-size:27px;color:var(--heading-grey);line-height:32px}
.welcome-title{font-weight:600;font-size:22px;color:var(--blue);line-height:28px}
.welcome p{font-size:11.2px;line-height:15.5px;margin-top:15px}
.welcome p:first-of-type{margin-top:14px}

.award{position:absolute;left:692px;top:580px;width:176px;height:124px;background:var(--badge)}

.service{position:absolute;top:762px;width:220px;height:200px;background:linear-gradient(180deg,#f4f4f4,#ffffff 40%,#f7f7f7);
  border-radius:6px;box-shadow:0 3px 6px rgba(0,0,0,.22);padding:14px 10px 0 15px}
.service-kicker{font-family:"Montserrat",Arial,sans-serif;font-weight:300;font-size:19px;color:var(--heading-grey);line-height:22px;padding-left:1px}
.service-title{font-family:"Montserrat",Arial,sans-serif;font-weight:400;font-size:24px;color:var(--blue);line-height:26px;padding-left:1px}
.service p{font-size:10.2px;line-height:15.3px;margin-top:8px;letter-spacing:-.1px}
.service a{display:block;margin-top:5px;font-size:10.5px;color:var(--blue-dark);text-decoration:none}
.service--water{left:116px}
.service--carpet{left:378px}
.service--rug{left:648px}

.site-footer{position:absolute;left:0;top:1025px;width:985px;height:143px;border-top:4px solid #cfd6dc;
  background:linear-gradient(180deg,#1577c9,#0b57a5)}
.footer-mark{position:absolute;left:468px;top:-38px;width:50px;height:50px;border-radius:50%;background:var(--blue);border:3px solid var(--white)}
.footer-label{font-family:"Montserrat",Arial,sans-serif;font-weight:600;font-size:11px;line-height:14px;color:var(--white);letter-spacing:.3px}
.footer-big{font-family:"Lora",Georgia,serif;font-style:italic;font-size:18px;line-height:24px;color:var(--white)}
.contact-left{position:absolute;left:116px;top:19px}
.contact-left .footer-label + .footer-big{margin-top:6px}
.contact-left .footer-big + .footer-label{margin-top:19px}
.contact-right{position:absolute;left:640px;top:19px;color:#dbe9f6;font-size:11.5px;line-height:17px}
.contact-right .addr{margin-top:6px;margin-bottom:8px}
.community{display:flex;gap:9px;margin-top:6px}
.community span{width:25px;height:25px;border-radius:3px;background:#cfe3f4}

.copyright{position:absolute;left:0;top:1168px;width:985px;height:32px;background:linear-gradient(#f2f2f2,#e6e6e6);
  text-align:center;font-size:11.5px;line-height:32px;color:#444}
</style>
</head>
<body>

<header class="site-header">
  <svg class="header-tab" width="985" height="140" viewBox="0 0 985 140" aria-hidden="true">
    <path d="M0 0 H985 V12 H700 C688 12 684 20 680 40 C674 75 664 92 628 94 H352 C316 92 306 75 300 40 C296 20 292 12 280 12 H0 Z" fill="#f4f5f6"/>
  </svg>
  <div class="brand">
    <span class="brand-mark"></span>
    <span class="brand-name">LoomRinsePro</span>
  </div>
  <nav class="main-nav">
    <a href="#" style="width:105px">Home</a>
    <a href="#" style="width:134px">About Us</a>
    <a href="#" style="width:156px">Rug Washing</a>
    <a href="#" style="width:178px">Water Damage</a>
    <a href="#" style="width:179px">Carpet Cleaning</a>
  </nav>
</header>

<section class="hero-band"></section>
<div class="hero-frame">
  <div class="hero-photo" role="img" aria-label="Rolled oriental rugs stacked beside an antique gold upholstered chair"></div>
</div>
<div class="slider-dots"><span class="active"></span><span></span><span></span><span></span></div>

<section class="welcome">
  <div class="welcome-kicker">Welcome to</div>
  <h1 class="welcome-title">LoomRinsePro Harborfresh Cleaning, LLC</h1>
  <p>When it comes to cleaning carpet, oriental rugs, area rugs or furniture - any fabric from antique silk brocades to contemporary carpet fibers - our service is unparalled.</p>
  <p>Harborfresh Cleaning &amp; Restoration is the recipient of the 2010 &amp; 2011 "Valley Service Honor" in Fenwick, Alabama for Water Damage Restoration and Carpet and Rug Cleaning.</p>
  <p>Please contact us for an extensive list of references.</p>
</section>

<div class="award" role="img" aria-label="Award seal"></div>

<article class="service service--water">
  <div class="service-kicker">Water Damage</div>
  <h2 class="service-title">Restoration</h2>
  <p>Trust the company that has been getting families back home and businesses back to work for over 20 years. Harborfresh is very proud to be one of the industry leaders in restorative drying and moisture control services.</p>
  <a href="#">Read more</a>
</article>
<article class="service service--carpet">
  <div class="service-kicker">Carpet &amp; Upholstery</div>
  <h2 class="service-title">Cleaning</h2>
  <p>Wool or synthetic, woven or tufted, residential or commercial, the experienced technicians at Harborfresh know how to restore your carpet's appearance... and to provide you with a healthier indoor enviroment.</p>
  <a href="#">Read more</a>
</article>
<article class="service service--rug">
  <div class="service-kicker">Fine Rug</div>
  <h2 class="service-title">Washing</h2>
  <p>Oriental and Speciality Rugs differ greatly in their construction, dyeing methods and fiber content... and we understand these differences, assuring a safe and thorough in-plant cleaning of your speciality rugs.</p>
  <a href="#">Read more</a>
</article>

<footer class="site-footer">
  <span class="footer-mark"></span>
  <div class="contact-left">
    <div class="footer-label">EMAIL</div>
    <div class="footer-big">office@harborfreshcare.example</div>
    <div class="footer-label">PHONE</div>
    <div class="footer-big">(555) 014-2290</div>
  </div>
  <div class="contact-right">
    <div class="footer-label">CONTACT US</div>
    <div class="addr">Harborfresh Cleaning &amp; Restoration<br>48 Quarry Lane Fenwick, AL 35000</div>
    <div class="footer-label">COMMUNITY</div>
    <div class="community"><span></span><span></span><span></span></div>
  </div>
</footer>

<div class="copyright">Copyright © 2012 LoomRinsePro Harborfresh Cleaning, LLC.</div>

</body>
</html>
```